Land Buying Company Needs Letterhead for Direct Mail Marketing to Land Owners

We are looking for a professional letterhead that we will be including in our direct mail marketing. We will be sending this to land owners who may be interested in selling or purchasing land.

The letterhead needs to be editable. Headers and footers would look nice, but we are open. We would want it to include our address, website, phone, and email info. For right now the address to use for design purposes would the following:

Address: 412 Fenwick Avenue #300
Dallas, TX 75319
Website - www.quillbrookacres.com
Email - info@quillbrookacres.com
Phone - 866-492-ACRE

I have attached our logo zip file that we just had done on Pixel Harbor. Let me know what questions you have, and thank you.

```html
<!DOCTYPE html>
<html lang="en">
<head>
<meta charset="utf-8">
<title>Quillbrook Acres Letterhead</title>
<link href="https://fonts.googleapis.com/css2?family=Montserrat:wght@700&family=Open+Sans:wght@400;600&display=swap" rel="stylesheet">
<style>
  :root {
    --backdrop: #e4ebd9;
    --paper: #ffffff;
    --leaf: #8cc63f;
    --forest: #4a7a22;
    --forest-deep: #3c6619;
    --ink: #3a3a3a;
    --watermark: #f1f1f1;
  }
  html, body {
    margin: 0;
    padding: 0;
    width: 1200px;
    height: 784px;
    overflow: hidden;
    background: var(--backdrop);
  }
  .letterhead {
    position: absolute;
    left: 314px;
    top: 22px;
    width: 572px;
    height: 740px;
    background: var(--paper);
    box-shadow: 0 4px 14px rgba(60, 80, 40, 0.18);
    overflow: hidden;
  }
  .header-rule,
  .footer-graphics {
    position: absolute;
    left: 0;
    display: block;
  }
  .header-rule { top: 0; }
  .footer-graphics { bottom: 0; }
  .brand {
    position: absolute;
    top: 30px;
    right: 30px;
    display: flex;
    align-items: center;
    gap: 10px;
  }
  .brand-dot {
    width: 30px;
    height: 30px;
    border-radius: 50%;
    background: var(--forest);
  }
  .brand-name {
    font-family: "Montserrat", sans-serif;
    font-weight: 700;
    font-size: 19px;
    letter-spacing: 1.5px;
    color: var(--leaf);
    line-height: 1;
  }
  .watermark {
    position: absolute;
    left: 136px;
    top: 220px;
    width: 300px;
    height: 300px;
    border-radius: 50%;
    background: var(--watermark);
  }
  .contact-line {
    position: absolute;
    left: 26px;
    bottom: 34px;
    display: flex;
    gap: 14px;
    font-family: "Open Sans", sans-serif;
    font-size: 8.5px;
    color: var(--ink);
    white-space: nowrap;
  }
  .contact-item {
    display: flex;
    align-items: center;
    gap: 4px;
  }
  .contact-icon {
    width: 9px;
    height: 9px;
  }
  .website {
    position: absolute;
    right: 20px;
    bottom: 6px;
    font-family: "Open Sans", sans-serif;
    font-weight: 600;
    font-size: 9px;
    color: var(--paper);
  }
</style>
</head>
<body>
  <div class="letterhead">
    <svg class="header-rule" width="572" height="80" viewBox="0 0 572 80">
      <polygon points="0,8 240,8 262,26 262,30 238,12 0,12" fill="var(--leaf)"/>
      <polygon points="538,72 572,72 572,80 546,80" fill="var(--forest)"/>
    </svg>

    <div class="brand">
      <span class="brand-dot"></span>
      <span class="brand-name">QUILLBROOK ACRES</span>
    </div>

    <div class="watermark" role="img" aria-label="Faint background seal"></div>

    <div class="contact-line">
      <span class="contact-item">
        <svg class="contact-icon" viewBox="0 0 10 10"><circle cx="5" cy="5" r="5" fill="var(--ink)"/><path d="M5 2a2 2 0 0 0-2 2c0 1.5 2 4 2 4s2-2.5 2-4a2 2 0 0 0-2-2z" fill="#fff"/></svg>
        412 Fenwick Avenue #300 Dallas, TX 75319
      </span>
      <span class="contact-item">
        <svg class="contact-icon" viewBox="0 0 10 10"><circle cx="5" cy="5" r="5" fill="var(--ink)"/><rect x="3.5" y="2.2" width="3" height="5.6" rx="0.6" fill="#fff"/></svg>
        866-492-ACRE
      </span>
      <span class="contact-item">
        <svg class="contact-icon" viewBox="0 0 10 10"><circle cx="5" cy="5" r="5" fill="var(--ink)"/><rect x="2.5" y="3.3" width="5" height="3.4" fill="#fff"/><path d="M2.5 3.3 5 5.3 7.5 3.3" stroke="var(--ink)" stroke-width="0.6" fill="none"/></svg>
        info@quillbrookacres.com
      </span>
    </div>

    <svg class="footer-graphics" width="572" height="30" viewBox="0 0 572 30">
      <polygon points="0,2 100,2 106,8 340,8 346,14 0,14" fill="var(--leaf)" opacity="0.9"/>
      <rect x="0" y="14" width="572" height="16" fill="var(--forest)"/>
      <polygon points="400,0 572,0 572,30 380,30 380,20" fill="var(--forest-deep)"/>
    </svg>
    <div class="website">www.quillbrookacres.com</div>
  </div>
</body>
</html>
```